Lantern Path Collective

Re-design our website www.lanternpathco.org
We are a non profit catering for adults, elderly, veterans and youth in impoverished neighborhoods to improve their digital access and help them improve their lives and better our community.

I need the text on home page to stay. Its the first message vsitors shd read when they arrive on our page.

Number of Pages Required

4 page

Font styles to use
Other font styles liked:
• color and font shd be like the image attched below.

```html
<!DOCTYPE html>
<html lang="en">
<head>
<meta charset="utf-8">
<title>Lantern Path Collective</title>
<link href="https://fonts.googleapis.com/css2?family=Jost:wght@400;500;600&family=Josefin+Sans:wght@400;600&display=swap" rel="stylesheet">
<style>
:root{
  --blue:#3d87e8;
  --peach:#f8c79b;
  --lime:#c6e09b;
  --lime-dark:#8fb85a;
  --ink:#222;
  --muted:#555;
  --white:#fff;
  --dark:#1c1c1c;
  --box-steel:#a9c7db;
  --box-sky:#c8dcf6;
}
*{box-sizing:border-box;margin:0;padding:0}
html,body{width:1200px;height:5259px;overflow:hidden}
body{font-family:"Jost",sans-serif;color:var(--ink);position:relative;background:var(--white)}
section,header,footer{position:absolute;left:0;width:1200px}
.abs{position:absolute}
.pill{display:inline-flex;align-items:center;justify-content:center;border-radius:22px;font-size:13px;font-weight:500}
.pill-lime{background:var(--lime);color:var(--ink)}
.pill-blue{background:var(--blue);color:var(--white)}
.brand{display:flex;align-items:center;gap:10px;color:var(--white);font-family:"Jost",sans-serif;font-weight:600;font-size:20px;line-height:1.1}
.brand-dot{width:22px;height:22px;border-radius:50%;background:var(--lime);flex:none}

/* header */
.site-header{top:0;height:160px;background:var(--blue)}
.nav{position:absolute;top:94px;left:465px;display:flex;gap:40px;font-size:14px;color:var(--white)}
.nav .active{color:var(--lime);border-bottom:2px solid var(--lime);padding-bottom:6px}
.call{position:absolute;left:818px;top:45px;display:flex;gap:8px;align-items:center;color:var(--white);font-size:11px;line-height:1.2}
.call-icon{width:26px;height:26px;border-radius:50%;background:var(--lime);display:flex;align-items:center;justify-content:center}
.donate-top{position:absolute;left:965px;top:36px;width:157px;height:42px;gap:22px;font-size:14px}

/* hero */
.hero{top:160px;height:640px;background:linear-gradient(100deg,#e8ef9e 0%,#b7d96d 40%,#8cc24a 75%,#d8e7a8 100%)}
.hero-art{position:absolute;left:470px;top:20px;width:720px;height:600px;border-radius:40% 40% 30% 30%;background:radial-gradient(ellipse at 50% 45%,#9fa7a4 0%,#6f8f58 45%,rgba(140,194,74,0) 72%)}
.hero h1{position:absolute;left:72px;top:243px;font-size:34px;font-weight:500;line-height:1.22;color:#2c2c2c;letter-spacing:.5px}
.hero p{position:absolute;left:75px;top:332px;font-size:12px;line-height:1.3;color:#333;width:360px}
.hero .donate{position:absolute;left:77px;top:388px;width:154px;height:38px}
.dots{position:absolute;left:1146px;top:272px;display:flex;flex-direction:column;gap:17px}
.dots i{width:9px;height:9px;border-radius:50%;background:var(--white);display:block}
.dots i.on{width:15px;height:15px;margin-left:-3px;border:3px solid var(--white);background:var(--blue)}

/* about */
.about{top:800px;height:636px;background:var(--blue);color:var(--white)}
.notch{position:absolute;left:540px;top:-4px}
.sec-title{position:absolute;left:0;width:1200px;text-align:center;font-size:32px;font-weight:500;letter-spacing:.5px}
.about-photo{position:absolute;left:110px;top:180px;width:468px;height:340px;border-radius:26px;background:linear-gradient(135deg,#e9d3b6,#c6d9e7 55%,#f2efe9);border:4px solid var(--white)}
.about-copy{position:absolute;left:628px;top:190px;width:462px;font-family:"Josefin Sans",sans-serif;font-size:12.5px;line-height:1.75}
.about-copy p{margin-bottom:17px}
.about .more{position:absolute;left:630px;top:479px;width:156px;height:38px}

/* services */
.services{top:1436px;height:682px;background:var(--peach)}
.services .sec-title{top:74px;color:#2c2c2c}
.card{position:absolute;top:154px;width:332px;height:446px;background:var(--white);border-radius:22px;overflow:hidden;text-align:center}
.card-img{height:232px}
.card h3{font-size:16px;font-weight:500;margin-top:26px;letter-spacing:.3px}
.card p{font-family:"Josefin Sans",sans-serif;font-size:12px;line-height:1.8;color:var(--muted);margin:22px 30px 0;height:66px}
.card .go{width:36px;height:36px;border-radius:50%;background:var(--lime);margin:18px auto 0;display:flex;align-items:center;justify-content:center}

/* access tabs */
.access{top:2118px;height:692px;background:var(--blue)}
.access h2{position:absolute;top:70px;width:1200px;text-align:center;color:var(--white);font-size:32px;font-weight:400;line-height:1.28}
.tabs{position:absolute;left:178px;top:172px;display:flex;gap:8px;align-items:flex-end}
.tab{height:40px;padding:0 20px;display:flex;align-items:center;font-size:13px;background:var(--peach);color:var(--ink)}
.tab.on{background:var(--white);height:44px}
.panel{position:absolute;left:110px;top:214px;width:978px;height:398px;background:var(--white);border-radius:24px}
.panel h3{position:absolute;left:48px;top:58px;width:450px;font-size:23px;font-weight:500;line-height:1.33}
.panel h4{position:absolute;left:48px;top:128px;font-size:15px;font-weight:500}
.panel p{position:absolute;left:48px;top:156px;width:430px;font-family:"Josefin Sans",sans-serif;font-size:12px;line-height:1.8;color:var(--muted)}
.panel .rm{position:absolute;left:48px;top:292px;width:154px;height:40px}
.panel .dn{position:absolute;left:216px;top:292px;width:154px;height:40px}
.panel-photo{position:absolute;left:526px;top:36px;width:410px;height:318px;border-radius:22px;background:linear-gradient(120deg,#e9d7c6,#c9a486 45%,#3e4c66)}

/* impact */
.impact{top:2810px;height:685px;background:radial-gradient(ellipse at 72% 50%,#6f7d63 0%,#3f4a38 40%,#1d2619 100%)}
.impact-art{position:absolute;left:620px;top:80px;width:360px;height:560px;border-radius:50% 50% 20% 20%;background:radial-gradient(ellipse at 50% 40%,#5c8a3a 0%,#4f6c38 40%,rgba(80,100,70,0) 72%)}
.impact h2{position:absolute;left:110px;top:180px;font-size:32px;font-weight:500;color:var(--white);line-height:1.25;width:480px}
.impact h4{position:absolute;left:112px;top:288px;width:420px;font-size:16px;font-weight:500;color:var(--white);line-height:1.3}
.impact p{position:absolute;left:112px;top:348px;width:470px;font-family:"Josefin Sans",sans-serif;font-size:12px;line-height:1.8;color:#e6e6e6}
.impact .rm{position:absolute;left:114px;top:534px;width:154px;height:38px}

/* explore */
.explore{top:3495px;height:668px;background:var(--blue);color:var(--white)}
.explore h2{position:absolute;top:92px;width:1200px;text-align:center;font-size:33px;font-weight:400;line-height:1.25}
.explore p{position:absolute;left:220px;top:214px;width:760px;text-align:center;font-family:"Josefin Sans",sans-serif;font-size:13px;line-height:1.75}
.tile{position:absolute;top:324px;width:235px;height:237px;border-radius:22px;text-align:center;color:#2c2c2c;font-size:14px;font-weight:500;letter-spacing:.3px}
.tile svg{position:absolute;left:70px;top:36px}
.tile span{position:absolute;left:10px;right:10px;top:160px;line-height:1.3}

/* contact */
.contact{top:4163px;height:680px;background:var(--peach)}
.contact .sec-title{top:164px;color:#2c2c2c}
.field{position:absolute;height:44px;background:var(--white);border-radius:6px;font-size:11px;color:#555;padding:17px 14px 0}
.contact .submit{position:absolute;left:529px;top:516px;width:154px;height:38px;font-size:11px}

/* footer */
.site-footer{top:4843px;height:416px;background:var(--dark);color:#ddd}
.site-footer h5{position:absolute;top:93px;font-size:15px;font-weight:500;color:var(--white);letter-spacing:.5px}
.site-footer h5::after{content:"";display:block;width:36px;height:2px;background:var(--white);margin-top:8px}
.links{position:absolute;left:342px;top:135px;list-style:none;font-size:13px;line-height:27px}
.links li::before{content:">";margin-right:10px}
.links .on{color:var(--lime)}
.info{position:absolute;left:571px;top:136px;font-size:12px;line-height:1.7;width:220px}
.info div{display:flex;gap:12px;margin-bottom:22px}
.map{position:absolute;left:870px;top:143px;width:256px;height:148px;background:linear-gradient(135deg,#eef0f4,#dfe7ee);}
.rule{position:absolute;left:74px;top:346px;width:1052px;height:1px;background:#444}
.copy{position:absolute;left:90px;top:373px;font-size:11px}
.social{position:absolute;left:946px;top:364px;display:flex;gap:12px}
.social i{width:34px;height:34px;border-radius:50%;background:var(--lime);display:block}
</style>
</head>
<body>

<header class="site-header">
  <div class="abs brand" style="left:72px;top:46px;width:200px">
    <span class="brand-dot"></span><span>Lantern Path<br>Collective</span>
  </div>
  <div class="call">
    <span class="call-icon"><svg width="12" height="12" viewBox="0 0 24 24"><path fill="#3d87e8" d="M6.6 10.8a15 15 0 0 0 6.6 6.6l2.2-2.2c.3-.3.7-.4 1-.2 1.1.4 2.3.6 3.6.6.6 0 1 .4 1 1V20c0 .6-.4 1-1 1A17 17 0 0 1 3 4c0-.6.4-1 1-1h3.5c.6 0 1 .4 1 1 0 1.3.2 2.5.6 3.6.1.3 0 .7-.2 1z"/></svg></span>
    <span>Call Us<br>555 014 2290</span>
  </div>
  <div class="pill pill-lime donate-top">Donate
    <svg width="40" height="10" viewBox="0 0 40 10"><path d="M0 5h37M32 1l5 4-5 4" stroke="#222" stroke-width="1.5" fill="none"/></svg>
  </div>
  <nav class="nav">
    <span class="active">Home</span><span>About</span><span>Get Connected</span><span>e-Waste Services</span><span>Our Impact</span><span>Contact</span>
  </nav>
</header>

<section class="hero">
  <div class="hero-art" role="img" aria-label="Open hand holding a pile of discarded electronics wrapped in green leaves"></div>
  <h1>CREATING A SOCIAL<br>IMPACT WITH E-WASTE</h1>
  <p>The word ‘Veloren’ originates from old Northumbrian English language and means ‘above, beyond’.</p>
  <div class="pill pill-blue donate">Donate</div>
  <div class="dots"><i></i><i class="on"></i><i></i><i></i></div>
</section>

<section class="about">
  <svg class="notch" width="120" height="36" viewBox="0 0 120 36">
    <path d="M0 0 C30 0 40 32 60 32 C80 32 90 0 120 0 Z" fill="#3d87e8"/>
  </svg>
  <svg class="abs" style="left:594px;top:-34px" width="12" height="40" viewBox="0 0 12 40"><path d="M6 0v38M1 32l5 6 5-6" stroke="#222" stroke-width="1.5" fill="none"/></svg>
  <h2 class="sec-title" style="top:100px">ABOUT US</h2>
  <div class="about-photo" role="img" aria-label="Children gathered around a laptop, smiling"></div>
  <div class="about-copy">
    <p>Lorem Ipsum is simply dummy text of the printing and typesetting industry has been the industry's standard dummy text ever since the 1500s,</p>
    <p>when an unknown printer took a galley of type and scrambled it to make a type specimen book. It has survived not only five centuries, but also the leap into electronic typesetting, remaining essentially unchanged. It was popularised in the 1960s</p>
    <p>with the release of Typeplate sheets containing Lorem Ipsum passages, and more recently with desktop publishing software like Quillset Layout including into electronic typesetting, remaining essentially unchanged. It was popularised versions of Lorem Ipsum.</p>
  </div>
  <div class="pill pill-lime more">Read More</div>
</section>

<section class="services">
  <h2 class="sec-title">OUR SERVICES</h2>
  <article class="card" style="left:74px">
    <div class="card-img" role="img" aria-label="Green recycling bin of old computers in a bright office" style="background:linear-gradient(160deg,#eef1f3,#c9d3d8 60%,#5fae4a)"></div>
    <h3>E-WASTE SERVICES</h3>
    <p>Lantern Path Collective makes it easy for businesses and organizations across different industries to do good by diverting...</p>
    <div class="go"><svg width="14" height="12" viewBox="0 0 14 12"><path d="M1 6h11M8 2l4 4-4 4" stroke="#222" stroke-width="1.8" fill="none"/></svg></div>
  </article>
  <article class="card" style="left:433px">
    <div class="card-img" role="img" aria-label="Stacks of discarded hard drives and laptops" style="background:linear-gradient(160deg,#d9dcde,#6e7377 55%,#2d3033)"></div>
    <h3>DATA DESTRUCTION</h3>
    <p>Data breaches cost companies an average of $4 million per instance and 80% of customers refuse to shop with companies...</p>
    <div class="go"><svg width="14" height="12" viewBox="0 0 14 12"><path d="M1 6h11M8 2l4 4-4 4" stroke="#222" stroke-width="1.8" fill="none"/></svg></div>
  </article>
  <article class="card" style="left:792px">
    <div class="card-img" role="img" aria-label="Worker placing old computer parts in a green bin" style="background:linear-gradient(160deg,#8cc0e0,#4d86b5 50%,#3f8a3c)"></div>
    <h3>TECHNOLOGY DRIVES</h3>
    <p>By hosting a Tech Drive for people at your organization or in your community, you're helping them safely dispose...</p>
    <div class="go"><svg width="14" height="12" viewBox="0 0 14 12"><path d="M1 6h11M8 2l4 4-4 4" stroke="#222" stroke-width="1.8" fill="none"/></svg></div>
  </article>
</section>

<section class="access">
  <h2>Access Devices, Internet, Digital Training,<br>&amp; Tech Support. Today.</h2>
  <div class="tabs">
    <div class="tab on">Get Technology</div>
    <div class="tab">Low-Cost Internet</div>
    <div class="tab">Digital Training</div>
    <div class="tab">Tech Support</div>
    <div class="tab">For Organizations</div>
  </div>
  <div class="panel">
    <h3>Set Up Your Community For Success in the 21st Century</h3>
    <h4>Empower Your Constituents with Digital Access</h4>
    <p>Community-based organizations see firsthand how the digital divide creates immense barriers for people to achieve basic tasks like change careers, pursue an education, or just stay connected with friends and family. By utilizing Lantern Path Collective's full suite of digital inclusion services, ...</p>
    <div class="pill pill-lime rm">Read More</div>
    <div class="pill pill-blue dn">Donate</div>
    <div class="panel-photo" role="img" aria-label="Students seated at computer keyboards in a classroom"></div>
  </div>
</section>

<section class="impact">
  <div class="impact-art" role="img" aria-label="Young tree growing out of a heap of discarded electronics under a cloudy sky"></div>
  <h2>Creating a Social Impact with<br>e&#8209;Waste</h2>
  <h4>by transforming Unwanted Technology into Opportunities for People In-Need.</h4>
  <p>Lantern Path Collective is a nonprofit and social enterprise that creates equitable access to opportunity by providing devices, internet access, digital skills training, and tech support for low-income families, the homeless, and Veterans in our communities while at the same time, empowering businesses and organizations to do good by diverting technology from landfills to protect our planet.</p>
  <div class="pill pill-lime rm">Read More</div>
</section>

<section class="explore">
  <h2>Explore Opportunities Online with<br>Low-Cost Technology, Internet, Training &amp; Support</h2>
  <p>In order to comprehensively shrink the digital divide, we offer you access to low-cost computers, low-cost internet, free digital literacy training and tech support. Click the boxes below to explore how we can help you and members of your community unlock their full potential through digital technology.</p>
  <div class="tile" style="left:110px;background:var(--lime)">
    <svg width="96" height="96" viewBox="0 0 96 96" fill="none" stroke="#222" stroke-width="2.5"><rect x="8" y="14" width="80" height="54" rx="3"/><path d="M36 82h24M48 68v14"/><circle cx="48" cy="40" r="10"/><path d="M48 22v6M48 52v6M30 40h6M60 40h6M35 27l4 4M57 49l4 4M35 53l4-4M57 31l4-4"/></svg>
    <span>AFFORDABLE<br>TECHNOLOGY</span>
  </div>
  <div class="tile" style="left:358px;background:var(--box-steel)">
    <svg width="96" height="96" viewBox="0 0 96 96" fill="none" stroke="#222" stroke-width="2.5"><circle cx="48" cy="48" r="38"/><ellipse cx="48" cy="48" rx="16" ry="38"/><path d="M10 48h76M16 30h64M16 66h64M48 10v76"/></svg>
    <span>INTERNET ACCESS</span>
  </div>
  <div class="tile" style="left:606px;background:var(--peach)">
    <svg width="96" height="96" viewBox="0 0 96 96" fill="none" stroke="#222" stroke-width="2.5"><rect x="10" y="12" width="76" height="56" rx="3"/><path d="M48 20v42M20 24h20M20 34h20M20 44h20M56 24h20M56 34h20M56 44h20M10 78h76M30 68v10M66 68v10"/></svg>
    <span>DIGITAL LITERACY<br>TRAINING</span>
  </div>
  <div class="tile" style="left:854px;background:var(--box-sky)">
    <svg width="96" height="96" viewBox="0 0 96 96" fill="none" stroke="#222" stroke-width="2.5"><path d="M18 50V42a30 30 0 0 1 60 0v8"/><rect x="10" y="46" width="14" height="22" rx="5"/><rect x="72" y="46" width="14" height="22" rx="5"/><path d="M79 68c0 10-10 14-22 14"/><circle cx="48" cy="50" r="9"/><path d="M48 34v6M48 60v6M32 50h6M58 50h6"/></svg>
    <span>TECH SUPPORT</span>
  </div>
</section>

<section class="contact">
  <h2 class="sec-title">QUICK CONTACT</h2>
  <div class="field" style="left:235px;top:236px;width:240px">First Name*</div>
  <div class="field" style="left:486px;top:236px;width:241px">Last Name*</div>
  <div class="field" style="left:737px;top:236px;width:241px">Phone*</div>
  <div class="field" style="left:235px;top:296px;width:743px">I'm interested in:*
    <svg class="abs" style="right:16px;top:19px" width="10" height="6" viewBox="0 0 10 6"><path d="M1 1l4 4 4-4" stroke="#333" stroke-width="1.4" fill="none"/></svg>
  </div>
  <div class="field" style="left:235px;top:352px;width:743px;height:140px">How can we help you today?*</div>
  <div class="pill pill-blue submit">SUBMIT</div>
</section>

<footer class="site-footer">
  <div class="abs brand" style="left:76px;top:110px;width:200px">
    <span class="brand-dot"></span><span>Lantern Path<br>Collective</span>
  </div>
  <h5 style="left:342px">QUICK LINKS</h5>
  <ul class="links">
    <li class="on">Home</li><li>About</li><li>Get Connected</li><li>e-Waste Services</li><li>Our Impact</li><li>Contact</li>
  </ul>
  <h5 style="left:571px">CONTACT INFO</h5>
  <div class="info">
    <div><svg width="12" height="12" viewBox="0 0 24 24"><path fill="#ddd" d="M6.6 10.8a15 15 0 0 0 6.6 6.6l2.2-2.2c.3-.3.7-.4 1-.2 1.1.4 2.3.6 3.6.6.6 0 1 .4 1 1V20c0 .6-.4 1-1 1A17 17 0 0 1 3 4c0-.6.4-1 1-1h3.5c.6 0 1 .4 1 1 0 1.3.2 2.5.6 3.6.1.3 0 .7-.2 1z"/></svg><span>(555) 014-2290</span></div>
    <div><svg width="12" height="12" viewBox="0 0 24 24"><rect x="2" y="5" width="20" height="14" fill="none" stroke="#ddd" stroke-width="2"/><path d="M2 5l10 8 10-8" fill="none" stroke="#ddd" stroke-width="2"/></svg><span>hello@lanternpathco.org</span></div>
    <div><svg width="12" height="14" viewBox="0 0 24 28"><path fill="#ddd" d="M12 0a10 10 0 0 0-10 10c0 8 10 18 10 18s10-10 10-18A10 10 0 0 0 12 0zm0 14a4 4 0 1 1 0-8 4 4 0 0 1 0 8z"/></svg><span>418 Alder Row, Millbrook,<br>CA 90000</span></div>
  </div>
  <h5 style="left:870px">LOCATION</h5>
  <div class="map" role="img" aria-label="Street map showing the office location"></div>
  <div class="rule"></div>
  <div class="copy">Copyright © 2021 <b>NORTHWICK STUDIO</b>. All Rights Reserved.</div>
  <div class="social" aria-label="Social media links"><i></i><i></i><i></i><i></i></div>
</footer>

</body>
</html>
```